Yummy Website Re-Design

We have a good website but no VERY GOOD :)

We would like improve the user experience, in shopping page particularly.

Target Market(s)

people 25-40 70% of girl (actually)

Industry/Entity Type

Shopping

Requirements
Must have
• Redesign of www.brunorla.ch
Same colors
Same logotype

1) Homepage
- With highlight product / offer (large display!)
- Space to explain the concept
- Delicious button call-to-action for order a breakfast

2) THE CONCEPT
- Page for explain the concept and team pictures (3persons)

3) COMPOSE !
- Shopping page with, on the top, the X package we offer (business pack, st valentine, christmas, family, etc.) (slider?)

- Then, the products (grid?) classified into categories, we would'like to display one photo / item, the name, the weight and the price.

If you want to add the product, you must choose the number of elements and add to cart

Please, suscribe and test the order process to view all step

4) DELIVERY ZONES
- Page with map of different delivery rate and possibility

5) FAQ

X) Footer with the same information what www.brunorla.ch

Yummy, delicious design (we delivery very delicious breakfast @home).

LET'S EXPLODE YOUR CREATIVITY WITH THIS WORDS : YUMMY, DELICIOUS, SWEET.

```html
<!DOCTYPE html>
<html lang="en">
<head>
<meta charset="utf-8">
<title>Brunorla – Breakfast in bed</title>
<link rel="stylesheet" href="https://fonts.googleapis.com/css2?family=Lobster+Two:ital,wght@1,700&family=Lora:wght@400;700&family=Noto+Serif:ital@1&family=Bree+Serif&family=Montserrat:wght@400;600&display=swap">
<style>
:root{
  --choc:#2f1711;
  --hero-red:#9a2410;
  --hero-deep:#4a120a;
  --cream:#f4f0e3;
  --cream-dark:#ece6d3;
  --paper:#fbfaf6;
  --tan:#c18b69;
  --tan-light:#caa07a;
  --tan-dark:#a77a57;
  --panel:#2b2725;
  --panel-line:#443d39;
  --olive:#a59c4f;
  --ribbon:#6f1d12;
  --ribbon-dark:#4d130b;
  --berry:#c8200f;
  --ink:#3a2a22;
  --grey:#7b756c;
  --white:#ffffff;
}
*{margin:0;padding:0;box-sizing:border-box}
html,body{width:686px;height:1200px;overflow:hidden}
body{position:relative;background:var(--cream);font-family:"Montserrat",sans-serif;color:var(--ink)}
.abs{position:absolute}
.top-band{left:0;top:0;width:686px;height:378px;background:var(--choc)}
.hero{left:80px;top:92px;width:524px;height:283px;background:radial-gradient(ellipse at 62% 45%,#b83015 0%,var(--hero-red) 35%,var(--hero-deep) 100%)}
.header{left:80px;top:0;width:524px;height:64px;background:linear-gradient(#fff,#f1eeea)}
.brand{left:12px;top:18px;display:flex;align-items:center;gap:8px;font-family:"Lora",serif;font-weight:700;font-size:26px;color:#6b3a22}
.brand-dot{width:14px;height:14px;border-radius:50%;background:#6b3a22}
.contact{right:12px;top:17px;text-align:right;font-size:8.5px;color:var(--grey);line-height:15px}
.contact b{font-size:13.5px;color:var(--berry);font-weight:600;margin-left:4px}
.contact a{color:var(--berry);text-decoration:none}
.phone-icon{left:424px;top:10px}
.nav{left:80px;top:64px;width:524px;height:28px;background:linear-gradient(var(--tan-light),var(--tan-dark));border-radius:0 0 5px 5px;display:flex}
.nav span{font-family:"Lora",serif;font-size:10.5px;color:var(--white);text-transform:uppercase;display:flex;align-items:center;justify-content:center;border-right:1px solid rgba(255,255,255,.35)}
.nav span:last-child{border:0}
.headline{font-family:"Lobster Two",cursive;font-style:italic;font-weight:700;color:var(--white);font-size:42px;line-height:1;text-shadow:0 2px 3px rgba(0,0,0,.45)}
.cta{left:119px;top:282px;width:159px;height:32px;border-radius:16px;background:linear-gradient(#f6f6f6,#b9b9b9);box-shadow:0 2px 4px rgba(0,0,0,.5);font-family:"Lora",serif;font-size:17px;color:#3a3a3a;display:flex;align-items:center;justify-content:center}
.slide-arrow{width:16px;height:16px;border-radius:50%;background:#8a7d78;top:211px}
.hero-photo{left:378px;top:118px;width:172px;height:220px;border-radius:40% 40% 30% 30%;background:radial-gradient(circle at 50% 45%,#e3b57c,#b77a3e 60%,#7a4a22)}
.welcome{left:80px;top:357px;width:524px;height:190px;background:var(--panel);border-radius:4px;padding:5px}
.welcome-inner{width:100%;height:100%;border:1px solid var(--panel-line);padding:14px 24px}
.welcome h1{font-family:"Lobster Two",cursive;font-style:italic;font-weight:700;font-size:27px;color:var(--white);margin-bottom:10px}
.welcome p{font-family:"Noto Serif",serif;font-style:italic;font-size:10px;line-height:13px;color:#d8d3cf;margin-bottom:11px}
.gallery-title{left:80px;top:578px;width:368px;text-align:center;font-family:"Lora",serif;font-size:13.5px;color:#6a2a18}
.gallery-title::before,.gallery-title::after{content:"";position:absolute;top:9px;width:110px;border-top:1px dashed #b9ad96}
.gallery-title::before{left:0}.gallery-title::after{right:0}
.product{width:96px;height:96px;border-radius:50%;top:612px;box-shadow:0 6px 6px -3px rgba(0,0,0,.35)}
.p1{left:106px;background:radial-gradient(circle at 40% 40%,#c99a6a,#7a4a2a)}
.p2{left:217px;background:radial-gradient(circle at 50% 50%,#e2b86a,#9c6a34)}
.p3{left:328px;background:radial-gradient(circle at 50% 50%,#d8a458,#8d5a26)}
.special{left:465px;top:578px;width:139px;height:138px;background:#241612;border-radius:4px;padding:3px}
.special-photo{width:100%;height:100%;background:radial-gradient(circle at 50% 35%,#f0e6da,#b98a66 55%,#5a3422);border-radius:2px}
.special-banner{left:467px;top:677px;width:139px;height:30px;background:var(--berry);font-family:"Lobster Two",cursive;font-style:italic;font-weight:700;font-size:19px;color:var(--white);display:flex;align-items:center;justify-content:center}
.steps{left:80px;top:766px;width:524px;height:170px;background:var(--tan);border-radius:5px;box-shadow:0 8px 8px -4px rgba(0,0,0,.3)}
.ribbon{left:155px;top:746px;width:390px;height:32px}
.ribbon-text{left:155px;top:746px;width:390px;height:30px;display:flex;align-items:center;justify-content:center;gap:6px;font-family:"Bree Serif",serif;font-size:14.5px;color:var(--white)}
.ribbon-badge{width:26px;height:26px;border-radius:50%;background:var(--olive);display:flex;align-items:center;justify-content:center;font-size:14px}
.step-circle{width:64px;height:64px;border-radius:50%;background:#f6f2e6;border:3px solid #e9e1cc;top:806px;box-shadow:0 2px 3px rgba(0,0,0,.25);display:flex;align-items:center;justify-content:center}
.step-num{width:26px;height:26px;border-radius:50%;background:var(--olive);border:2px solid #f6f2e6;top:849px;color:var(--white);font-family:"Bree Serif",serif;font-size:13px;display:flex;align-items:center;justify-content:center}
.step-label{top:884px;width:130px;text-align:center;font-family:"Bree Serif",serif;font-size:12px;line-height:16px;color:var(--white)}
.footer{left:0;top:990px;width:686px;height:138px;background:var(--cream-dark);border-top:1px solid #e2dbc6}
.col-title{top:1010px;width:190px;text-align:center;font-family:"Bree Serif",serif;font-size:12px;color:var(--ink)}
.col-text{width:160px;text-align:center;font-size:7px;line-height:10px;color:var(--grey)}
.card{top:1037px;width:22px;height:15px;border-radius:2px}
.field{left:476px;width:127px;height:17px;background:#dcd8c6;font-size:7.5px;color:#6c675d;padding:4px 8px}
.subscribe{left:508px;top:1080px;width:62px;height:18px;background:#7a3512;border-radius:2px;font-family:"Bree Serif",serif;font-size:10.5px;color:var(--white);display:flex;align-items:center;justify-content:center}
.bottom{left:0;top:1128px;width:686px;height:72px;background:#f3efe3}
.links{top:1137px;width:686px;text-align:center;font-size:8px;color:#5f5a52;word-spacing:2px}
.copy{top:1149px;width:686px;text-align:center;font-size:8px;color:#5f5a52}
.social{top:1165px;width:24px;height:24px;border-radius:50%;background:#d8d4ca}
</style>
</head>
<body>
<div class="abs top-band"></div>
<div class="abs hero"></div>

<header class="abs header">
  <div class="abs brand"><span class="brand-dot"></span>Brunorla</div>
  <div class="abs contact">Contact us on <b>022 555 0148</b><br>or email us <a>hello@brunorla.ch</a></div>
</header>
<svg class="abs phone-icon" width="30" height="42" viewBox="0 0 30 42"><path d="M10 2c-6 3-8 12-6 22s7 15 12 14l2-7-6-3c-2-4-3-8-2-12l6-2-1-8z" fill="#2a2a2a"/><path d="M16 38c4 2 8 2 12 0" stroke="#2a2a2a" stroke-width="1.5" fill="none"/></svg>

<nav class="abs nav">
  <span style="width:85px">Home</span>
  <span style="width:124px">The Concept</span>
  <span style="width:103px">Compose</span>
  <span style="width:139px">Dilivery Zones</span>
  <span style="width:73px">FAQ</span>
</nav>

<div class="abs headline" style="left:106px;top:120px">Yummy</div>
<div class="abs headline" style="left:145px;top:168px">Delicious</div>
<div class="abs headline" style="left:183px;top:213px">Sweet</div>
<div class="abs cta">Order A Breakfast</div>
<div class="abs hero-photo" role="img" aria-label="Basket of assorted breads and rolls"></div>
<div class="abs slide-arrow" style="left:80px"></div>
<div class="abs slide-arrow" style="left:588px"></div>
<svg class="abs" style="left:80px;top:211px" width="16" height="16"><path d="M10 4 5 8l5 4" stroke="#fff" stroke-width="2" fill="none"/></svg>
<svg class="abs" style="left:588px;top:211px" width="16" height="16"><path d="M6 4l5 4-5 4" stroke="#fff" stroke-width="2" fill="none"/></svg>

<section class="abs welcome">
  <div class="welcome-inner">
    <h1>Welcome to Brunorla</h1>
    <p>We are a company from Geneva, the first and only to offer to bring you the best buffet breakfast in bed.</p>
    <p>Whether you have guests, a large family or just your lover, love to treat or impress, we are at your disposal!</p>
    <p>Amazing cakes, crispy croissants, chocolate lollipops to get up at night, in short, a better breakfast than hotel, delivered to your door as you wish!</p>
    <p>Find out more about our offer on the page FAQ or place an order now!</p>
  </div>
</section>

<div class="abs gallery-title">PRODUCT GALLERY</div>
<svg class="abs" style="left:78px;top:640px" width="16" height="40"><path d="M13 2 3 20l10 18" stroke="#333" stroke-width="1.5" fill="none"/></svg>
<svg class="abs" style="left:436px;top:640px" width="16" height="40"><path d="M3 2l10 18L3 38" stroke="#333" stroke-width="1.5" fill="none"/></svg>
<div class="abs product p1" role="img" aria-label="Assorted bread rolls"></div>
<div class="abs product p2" role="img" aria-label="Golden croissant"></div>
<div class="abs product p3" role="img" aria-label="Small sweet pastries"></div>
<div class="abs special"><div class="special-photo" role="img" aria-label="Cup of hot chocolate with a muffin"></div></div>
<div class="abs special-banner">Weekly Special</div>

<section class="abs steps"></section>
<svg class="abs ribbon" viewBox="0 0 390 32" preserveAspectRatio="none"><path d="M0 6h20v26H0l8-13z" fill="var(--ribbon-dark)"/><path d="M390 6h-20v26h20l-8-13z" fill="var(--ribbon-dark)"/><rect x="12" y="0" width="366" height="28" fill="var(--ribbon)"/></svg>
<div class="abs ribbon-text">ORDER YOUR BRUNORLA IN <span class="ribbon-badge">4</span> STEPS</div>

<svg class="abs" style="left:80px;top:820px" width="524" height="30"><g stroke="#d9ad8e" stroke-dasharray="3 3" fill="none"><path d="M90 15h40M223 15h40M356 15h40"/></g><g stroke="#d9ad8e" fill="none"><path d="M125 9l6 6-6 6M258 9l6 6-6 6M391 9l6 6-6 6"/></g></svg>

<div class="abs step-circle" style="left:103px"><svg width="30" height="24" viewBox="0 0 30 24"><path d="M4 4h18v8a8 8 0 0 1-8 8h-2a8 8 0 0 1-8-8z" fill="var(--olive)"/><path d="M22 7h3a3 3 0 0 1 0 6h-3" stroke="var(--olive)" stroke-width="2" fill="none"/><rect x="0" y="21" width="28" height="3" rx="1.5" fill="var(--olive)"/></svg></div>
<div class="abs step-circle" style="left:236px"><svg width="26" height="24" viewBox="0 0 26 24"><path d="M1 2h4l3 13h13l3-9H7" stroke="var(--olive)" stroke-width="2.2" fill="none"/><circle cx="10" cy="20" r="2.2" fill="var(--olive)"/><circle cx="19" cy="20" r="2.2" fill="var(--olive)"/></svg></div>
<div class="abs step-circle" style="left:369px"><svg width="26" height="18" viewBox="0 0 26 18"><rect width="26" height="18" rx="2" fill="var(--olive)"/><rect y="4" width="26" height="3" fill="#f6f2e6"/><rect x="3" y="11" width="8" height="2" fill="#f6f2e6"/></svg></div>
<div class="abs step-circle" style="left:501px"><svg width="34" height="26" viewBox="0 0 34 26"><g stroke="var(--olive)" stroke-width="2" fill="none"><circle cx="7" cy="19" r="6"/><circle cx="27" cy="19" r="6"/><path d="M7 19l6-8h8l6 8M13 11l4 8h4"/></g><circle cx="19" cy="3" r="2.5" fill="var(--olive)"/></svg></div>

<div class="abs step-num" style="left:156px">1</div>
<div class="abs step-num" style="left:289px">2</div>
<div class="abs step-num" style="left:422px">3</div>
<div class="abs step-num" style="left:554px">4</div>
<div class="abs step-label" style="left:74px">Prepare<br>your Brunorla</div>
<div class="abs step-label" style="left:206px">Choose the date &amp;<br>time of delivery</div>
<div class="abs step-label" style="left:339px">Select the<br>payment method</div>
<div class="abs step-label" style="left:472px">Enjoy!</div>

<footer class="abs footer"></footer>
<div class="abs col-title" style="left:64px">Secure Payment</div>
<div class="abs card" style="left:96px;background:#dfe8f2"></div>
<div class="abs card" style="left:122px;background:#3a3a3a"></div>
<div class="abs card" style="left:148px;background:#2c4c8c"></div>
<div class="abs card" style="left:174px;background:#8fb6d8"></div>
<div class="abs card" style="left:200px;background:#f2d23a"></div>
<div class="abs col-text" style="left:79px;top:1071px">Quickly and easily pay your order by credit card secure platform with PayNest. We accept payment by Vantra, Cardora or Amerix Pay.</div>

<div class="abs col-title" style="left:262px">Delivery Throughout Geneva</div>
<svg class="abs" style="left:332px;top:1033px" width="56" height="28" viewBox="0 0 56 28"><rect x="14" y="0" width="42" height="20" fill="var(--olive)"/><path d="M0 10l5-7h8v17H0z" fill="var(--olive)"/><circle cx="9" cy="23" r="4" fill="var(--olive)" stroke="var(--cream-dark)" stroke-width="1.5"/><circle cx="44" cy="23" r="4" fill="var(--olive)" stroke="var(--cream-dark)" stroke-width="1.5"/></svg>
<div class="abs col-text" style="left:277px;top:1069px">Delivery from 4 CHF, see our prices on our different delivery! More</div>

<div class="abs col-title" style="left:443px">Our Newsletter!</div>
<div class="abs field" style="top:1033px">Enter Your Name</div>
<div class="abs field" style="top:1057px">Enter Your Email</div>
<div class="abs subscribe">SUBSCRIBE</div>

<div class="abs bottom"></div>
<div class="abs links">Home &nbsp;| &nbsp;The Concept &nbsp;| &nbsp;Compose &nbsp;| &nbsp;Dilivery Zones &nbsp;| &nbsp;FAQ</div>
<div class="abs copy">Copyright ©2012 Brunorla. All Rights Reserved</div>
<div class="abs social" style="left:324px"></div>
<div class="abs social" style="left:353px"></div>
</body>
</html>
```